New Business Card Design Project

Need a design that will create an impact / strong impression towards our clients for our business. We are in the lighting business and we do lighting retrofits for large commercial to industrial clientele.

Target Market(s)

Lighting Industry

Industry/Entity Type

Business

Other font styles liked:
• we would like to use the font on our logo, not sure what it is though..

Requirements
Must have
• Our logo.
Nice to have
• We are open to suggestions that have to do with lighting.

```html
<!DOCTYPE html>
<html lang="en">
<head>
<meta charset="utf-8">
<title>Lumen Retrofit Group – Business Card</title>
<link rel="stylesheet" href="https://fonts.googleapis.com/css2?family=Source+Sans+3:wght@400;600;700&display=swap">
<style>
  :root {
    --bg: #e4e5e7;
    --paper: #ffffff;
    --green-dark: #1b5e33;
    --green: #1e7a3e;
    --green-bright: #138a43;
    --green-light: #6cc04a;
    --ink: #4a4a4a;
    --rule: #9a9a9a;
    --white: #ffffff;
  }
  * { box-sizing: border-box; margin: 0; padding: 0; }
  html, body {
    width: 1200px; height: 800px; overflow: hidden;
    background: var(--bg);
    font-family: "Source Sans 3", "Myriad Pro", sans-serif;
  }
  .canvas {
    position: relative; width: 1200px; height: 800px;
    display: flex; align-items: center; justify-content: center; gap: 60px;
  }
  .card {
    position: relative; width: 520px; height: 297px;
    box-shadow: 0 6px 18px rgba(0,0,0,0.12);
  }
  .card--front { background: var(--paper); }
  .card--back {
    background: radial-gradient(ellipse at 50% 45%, var(--green-bright) 0%, var(--green) 45%, var(--green-dark) 100%);
    display: flex; align-items: center; justify-content: center;
  }
  .holder { position: absolute; left: 30px; top: 28px; }
  .holder__name {
    color: var(--green); font-weight: 700; font-size: 20px; letter-spacing: 0.5px;
  }
  .holder__title { color: var(--ink); font-size: 14px; margin-top: -2px; }
  .contact {
    position: absolute; left: 168px; top: 50px;
    border-left: 1px solid var(--rule); padding-left: 10px;
    font-size: 14px; color: var(--ink); line-height: 1.3;
  }
  .contact__row span { color: var(--green-bright); display: inline-block; width: 22px; }
  .contact__address { margin-top: 8px; }
  .brand {
    display: flex; align-items: center; gap: 10px;
    font-weight: 700; letter-spacing: 1px;
  }
  .brand__mark { width: 14px; height: 14px; }
  .brand__name { font-size: 30px; line-height: 1; }
  .brand__sub { font-size: 12px; letter-spacing: 2px; margin-top: 4px; }
  .card--front .brand { position: absolute; right: 40px; bottom: 38px; color: var(--green); }
  .card--front .brand__mark { background: var(--green-light); }
  .card--back .brand { color: var(--white); }
  .card--back .brand__mark { background: var(--white); }
</style>
</head>
<body>
<main class="canvas">
  <section class="card card--front" aria-label="Card front">
    <div class="holder">
      <p class="holder__name">JOHN DOE</p>
      <p class="holder__title">Director</p>
    </div>
    <div class="contact">
      <p class="contact__row"><span>T :</span>+63 900 5550123</p>
      <p class="contact__row"><span>E :</span>john@lumenretrofit.com</p>
      <p class="contact__row"><span>W :</span>www.lumenretrofit.com</p>
      <p class="contact__address">Dummy Street, Dummy City<br>Dummy Country</p>
    </div>
    <div class="brand">
      <div class="brand__mark"></div>
      <div>
        <p class="brand__name">LUMEN</p>
        <p class="brand__sub">LUMEN RETROFIT GROUP</p>
      </div>
    </div>
  </section>
  <section class="card card--back" aria-label="Card back">
    <div class="brand">
      <div class="brand__mark"></div>
      <div>
        <p class="brand__name">LUMEN</p>
        <p class="brand__sub">LUMEN RETROFIT GROUP</p>
      </div>
    </div>
  </section>
</main>
</body>
</html>
```